Labels for Bees Wax Candles & Honey Jars

We need labels for jars of natural honey. Most of our jars are square and the labels about 2" by 2".

Also we make bees wax candles of various sizes. We wish to wrap th enables around the circular candles which are between 2" and 3" in diameter... thus another have inch per label so they can be attached adhesively. The candles also vary in height... therefor th enables need to be 1.5", 2" and 3" in height.

We ar elooking for a very artistic and simple label that may include vibrant colors.
The name of our company must be displayed.. Candles by Morrow and for the Honey.... Morrow's All Natural Honey
Updates

The labels will be used for both Honey Jars as well as Bees Wax candles. There will be various sizes but that is something that can be adjusted after the initial design is approved. The Honey Jars should read "Natural Honey by Morrow" and the Candle labels should read "Natural Bees Wax Candles by Morrow" I am interested in simple, colorful, legible, and arty labels that pertain to bees and the natural environment. Hope this helps. We may also use a similar design on our web page. The size of the label on the honey will be 2" by 2" and the candles will vary.

Target Market(s)

Individual that purchase natural and organic products.

Requirements
Must have
• Labels should be very creative but legible and the emphasis on the candles should be all natural bees wax and the emphasis on the honey should be all natural honey. We are talking about the same design but different sizes and names.
Nice to have
• brillant colors and artistic

```html
<!DOCTYPE html>
<html lang="en">
<head>
<meta charset="utf-8">
<title>Morrow Honey &amp; Bees Wax Candle Labels</title>
<link rel="stylesheet" href="https://fonts.googleapis.com/css2?family=Bodoni+Moda:wght@500&family=Pinyon+Script&display=swap">
<style>
  :root {
    --paper: #ffffff;
    --frame: #bfb59c;
    --ink-brown: #6b4f3a;
    --ink-orange: #e0914a;
    --ink-blue: #9aa8c8;
    --swatch-pink: #ecb3c6;
    --swatch-orange: #e08532;
    --swatch-yellow: #ffbd3a;
    --swatch-plum: #6c3860;
    --swatch-rose: #c98387;
    --swatch-mauve: #c283a6;
    --serif: "Bodoni Moda", "Didot", serif;
    --script: "Pinyon Script", cursive;
  }
  html, body { margin: 0; padding: 0; overflow: hidden; }
  body { width: 1200px; height: 1000px; background: var(--paper); position: relative; }

  .panel { position: absolute; }
  .panel svg { display: block; width: 100%; height: 100%; }

  .pattern-fill {
    position: absolute; inset: 0;
    background: linear-gradient(135deg, var(--swatch-mauve) 0%, var(--swatch-yellow) 30%, var(--swatch-pink) 55%, var(--swatch-orange) 78%, var(--swatch-plum) 100%);
  }
  .panel svg.label-art { position: absolute; inset: 0; }

  .honey-label { left: 118px; top: 69px; width: 470px; height: 470px; }
  .jar-photo {
    left: 616px; top: 69px; width: 470px; height: 470px;
    background: linear-gradient(180deg, #f1f1ef 0%, #e9ebe7 60%, #dfe8cf 78%, #e8a33a 90%, #d9dfc6 100%);
  }
  .candle-label { left: 118px; top: 566px; width: 566px; height: 375px; }

  .title { font-family: var(--serif); font-weight: 500; }
  .title-brown { fill: var(--ink-brown); }
  .title-orange { fill: var(--ink-orange); }
  .maker { font-family: var(--script); fill: var(--ink-blue); }

  .palette { position: absolute; left: 770px; top: 648px; width: 250px; }
  .palette-title {
    margin: 0 0 26px; text-align: center;
    font-family: var(--serif); font-weight: 500; font-size: 17px;
    letter-spacing: 0.5px; color: var(--ink-orange);
  }
  .swatches { display: grid; grid-template-columns: repeat(3, 72px); gap: 19px 16px; justify-content: center; margin-left: -6px; }
  .swatch { width: 72px; height: 72px; border-radius: 50%; }
  .swatch.pink { background: var(--swatch-pink); }
  .swatch.orange { background: var(--swatch-orange); }
  .swatch.yellow { background: var(--swatch-yellow); }
  .swatch.plum { background: var(--swatch-plum); }
  .swatch.rose { background: var(--swatch-rose); }
  .swatch.mauve { background: var(--swatch-mauve); }
</style>
</head>
<body>

<section class="panel honey-label">
  <div class="pattern-fill" role="img" aria-label="Geometric triangle pattern in pink, plum, orange and yellow"></div>
  <svg class="label-art" viewBox="0 0 470 470">
    <polygon points="37,235 144,79 327,79 434,235 327,421 144,421" fill="var(--frame)" stroke="#fff" stroke-width="3"/>
    <polygon points="52,235 152,90 319,90 419,235 319,410 152,410" fill="none" stroke="#fff" stroke-width="2"/>
    <polygon points="62,235 157,100 314,100 409,235 314,400 157,400" fill="#fff" stroke="var(--ink-brown)" stroke-width="1"/>
    <text class="maker" x="235" y="180" text-anchor="middle" font-size="34">Morrow's</text>
    <text class="title title-brown" x="235" y="233" text-anchor="middle" font-size="42">All Natural</text>
    <text class="title title-orange" x="235" y="285" text-anchor="middle" font-size="42">Honey</text>
    <line x1="120" y1="317" x2="350" y2="317" stroke="var(--ink-brown)" stroke-width="1.5"/>
    <rect x="182" y="310" width="106" height="14" fill="var(--ink-brown)" role="img" aria-label="Small diamond ornament"/>
  </svg>
</section>

<div class="panel jar-photo" role="img" aria-label="Photograph of a honey jar wearing the label, with a dipper dripping honey onto a pale green plate"></div>

<section class="panel candle-label">
  <div class="pattern-fill" role="img" aria-label="Geometric triangle pattern in pink, plum, orange and yellow"></div>
  <svg class="label-art" viewBox="0 0 566 375">
    <path d="M74,70 H494 A20,20 0 0 0 514,90 V299 A20,20 0 0 0 494,319 H74 A20,20 0 0 0 54,299 V90 A20,20 0 0 0 74,70 Z" fill="var(--frame)" stroke="#fff" stroke-width="3"/>
    <path d="M84,82 H484 A14,14 0 0 0 498,96 V293 A14,14 0 0 0 484,307 H84 A14,14 0 0 0 70,293 V96 A14,14 0 0 0 84,82 Z" fill="#fff" stroke="var(--ink-brown)" stroke-width="1"/>
    <text class="title title-brown" x="284" y="149" text-anchor="middle" font-size="34">Natural Bees Wax</text>
    <text x="284" y="193" text-anchor="middle">
      <tspan class="title title-orange" font-size="34">Candles</tspan><tspan class="title title-brown" font-size="24"> by</tspan>
    </text>
    <text class="maker" x="284" y="234" text-anchor="middle" font-size="32">Morrow</text>
    <line x1="128" y1="262" x2="442" y2="262" stroke="var(--ink-brown)" stroke-width="1.5"/>
    <rect x="240" y="255" width="88" height="14" fill="var(--ink-brown)" role="img" aria-label="Small diamond ornament"/>
  </svg>
</section>

<section class="palette">
  <h2 class="palette-title">COLOUR PATTERN</h2>
  <div class="swatches">
    <span class="swatch pink"></span>
    <span class="swatch orange"></span>
    <span class="swatch yellow"></span>
    <span class="swatch plum"></span>
    <span class="swatch rose"></span>
    <span class="swatch mauve"></span>
  </div>
</section>

</body>
</html>
```